K.E.L Ventures - Business Card

We need a business card design for a new company based in Malaysia, called K.E.L Ventures Sdn. Bhd. We create, develop & customize database & software/web-based business systems to suit our clients need, mainly in oil&gas industry.

We would like to challenge the creativity of you to design a simple, meaningful, modern, professional & sleek. The design concept may varies but worthy enough for the recipients to proudly keep it in their wallet, and award us with fruitful business opportunities.

B-3-12 Meridan Plaza,
SS21/4, Subang Jaya,
46300 Selangor. Malaysia

http://kelventures-example.com

HAFIZ Roslan | +6012-3817260 | Co-Founder
Di Nazwan | +6012-4092731 | Co-Founder
Abdul Kamil | +6019-5063184 | Managing Director

Target Market(s)

The target market will expand to several other industries such as aviation, communication, automotive, education & hotel.

Industry/Entity Type

Business

Font styles to use
Serif
Sans Serif
Decorative
Script

Requirements
Must have
• plain background yet colourful concept.
Should not have
• something too easy that I can draw myself

```html
<!DOCTYPE html>
<html lang="en">
<head>
<meta charset="utf-8">
<title>K.E.L Ventures – Business Card</title>
<link rel="stylesheet" href="https://fonts.googleapis.com/css2?family=Source+Sans+3:wght@400;600;700&display=swap">
<style>
  :root {
    --page: #ffffff;
    --maroon: #5d0f1c;
    --maroon-deep: #4a0a15;
    --band: #e6e6e6;
    --ink: #1a1a1a;
    --white: #ffffff;
    --orange: #f5a01a;
    --orange-light: #ffc94a;
    --orange-deep: #e37a0c;
    --icon: #7a1a22;
  }
  * { margin: 0; padding: 0; box-sizing: border-box; }
  html, body { width: 1200px; height: 695px; overflow: hidden; background: var(--page); }
  body { font-family: "Source Sans 3", "Myriad Pro", Arial, sans-serif; position: relative; }

  .card {
    position: absolute; left: 80px; top: 46px;
    width: 990px; height: 564px;
    background: var(--maroon);
  }
  .brand {
    position: absolute; left: 0; right: 0; top: 62px;
    text-align: center;
    font-size: 64px; font-weight: 600; color: var(--orange);
    letter-spacing: 1px;
  }

  .contact { position: absolute; left: 0; width: 990px; height: 60px; }
  .contact--1 { top: 188px; }
  .contact--2 { top: 266px; }
  .contact--3 { top: 344px; }

  .person {
    position: absolute; left: 188px; width: 300px; text-align: center; color: var(--white);
  }
  .person__name { font-size: 27px; font-weight: 400; line-height: 32px; display: inline-block; }
  .contact--1 .person__name { border-bottom: 2px solid var(--white); line-height: 28px; }
  .person__role { font-size: 17px; line-height: 22px; }

  .arrow { position: absolute; left: 468px; top: 10px; width: 66px; height: 14px; }
  .phone {
    position: absolute; left: 566px; top: 2px;
    font-size: 23px; color: var(--white); letter-spacing: 0.5px;
  }
  .contact--2 .phone, .contact--3 .phone { left: 578px; }
  .contact--2 .arrow, .contact--3 .arrow { left: 472px; }

  .info-band {
    position: absolute; left: 0; top: 439px; width: 990px; height: 100px;
    background: var(--band);
  }
  .address {
    position: absolute; left: 102px; top: 14px;
    font-size: 23px; line-height: 27px; color: var(--ink);
  }
  .icon-home { position: absolute; left: 30px; top: 38px; width: 50px; height: 36px; }
  .icon-web { position: absolute; left: 554px; top: 33px; width: 52px; height: 40px; }
  .website {
    position: absolute; left: 622px; top: 34px;
    font-size: 24px; font-weight: 600; color: var(--ink);
  }
  .footer-strip {
    position: absolute; left: 0; top: 539px; width: 990px; height: 25px;
    background: var(--maroon-deep);
  }
</style>
</head>
<body>
  <section class="card">
    <div class="brand">K.E.L Ventures</div>

    <svg width="0" height="0" style="position:absolute">
      <defs>
        <linearGradient id="arrowFill" x1="0" y1="0" x2="0" y2="1">
          <stop offset="0" stop-color="#ffc94a"/>
          <stop offset="1" stop-color="#e37a0c"/>
        </linearGradient>
      </defs>
    </svg>

    <div class="contact contact--1">
      <div class="person">
        <div class="person__name">HAFIZ Roslan</div>
        <div class="person__role">Co-Founder</div>
      </div>
      <svg class="arrow" viewBox="0 0 66 14"><path d="M0 4 H54 V0 L66 7 L54 14 V10 H0 Z" fill="url(#arrowFill)"/></svg>
      <div class="phone">+6012-3817260</div>
    </div>

    <div class="contact contact--2">
      <div class="person">
        <div class="person__name">Di Nazwan</div>
        <div class="person__role">Co-Founder</div>
      </div>
      <svg class="arrow" viewBox="0 0 66 14"><path d="M0 4 H54 V0 L66 7 L54 14 V10 H0 Z" fill="url(#arrowFill)"/></svg>
      <div class="phone">+6012-4092731</div>
    </div>

    <div class="contact contact--3">
      <div class="person">
        <div class="person__name">Abdul Kamil</div>
        <div class="person__role">Managing Director</div>
      </div>
      <svg class="arrow" viewBox="0 0 66 14"><path d="M0 4 H54 V0 L66 7 L54 14 V10 H0 Z" fill="url(#arrowFill)"/></svg>
      <div class="phone">+6019-5063184</div>
    </div>

    <div class="info-band">
      <svg class="icon-home" viewBox="0 0 50 36" aria-hidden="true">
        <path d="M25 2 L2 18 H9 V34 H20 V24 H30 V34 H41 V18 H48 Z" fill="var(--icon)"/>
      </svg>
      <div class="address">
        B-3-12 Meridan Plaza,<br>
        SS21/4, Subang Jaya,<br>
        46300 Selangor. Malaysia
      </div>
      <svg class="icon-web" viewBox="0 0 52 40" aria-hidden="true">
        <rect x="2" y="2" width="48" height="36" rx="3" fill="none" stroke="var(--icon)" stroke-width="3"/>
        <circle cx="26" cy="20" r="11" fill="none" stroke="var(--icon)" stroke-width="2.5"/>
        <path d="M15 20 H37 M26 9 V31 M19 13 H33 M19 27 H33" stroke="var(--icon)" stroke-width="2" fill="none"/>
      </svg>
      <div class="website">http://kelventures-example.com</div>
    </div>
    <div class="footer-strip"></div>
  </section>
</body>
</html>
```